KELVANE HOMES & ASSOCIATES T.W.P.

I am wanting a classy double sided black standard size card with Metalic Rose gold for both the logo and lettering (name) on the front then my picture and contact info on the back.
The logo has a circle that is a sun symbol and that needs to be in METALIC GOLD AT THE TOP AND CASCADE TO rose gold then the line under it needs to be yellow METALIC gold The lettering on the front also to be Rose gold metalic. The back side with picture and phone # needs to be ROSE gold metalic
INFO FOR BACK OF CARD WITH PICTURE AND BLACK BACK ROUND
front
Mirela Jostad Realtor
back
license 07418923
email | mirela.jostad@kelvanehomes.example
c. 555.218.4790
f. 555.634.0182
web kelvanehomes.example
812 Larkmoor DR. Vista Calif. 92000

Target Market(s)

REAL ESTATE

Industry/Entity Type

REAL ESTATE

Contact Information for Business Card

NAME ON FRONT Mirela Jostad Agent BACK pic in corner with mirela.jostad@kelvanehomes.example

Font styles to use
Serif

Requirements
Must have
• BLACK FRONT AND BACK WITH METALIC ROSE GOLD LETTERING SEE EXAMPLE BELOW IN PICS
Nice to have
• I WOULD LIKE TO HAVE THE LOGO IN ROSE GOLD METALIC AND THE LINE UNDER THE CIRCLE TO BE IN YELLOW metalic GOLD. TO GIVE IT A SUN SET AFFECT ONLY MY NAME AND TITLE ON THE FRONT with a line on top AND THEN MY CONTACT INFO ON THE BACK
Should not have
• COLORS OTHER THAN BLACK , CHARCOLE AND METALIC LETTERS

```html
<!DOCTYPE html>
<html lang="en">
<head>
<meta charset="utf-8">
<title>Kelvane Homes – Mirela Jostad business cards</title>
<link rel="stylesheet" href="https://fonts.googleapis.com/css2?family=Figtree:wght@300;400&display=swap">
<style>
  :root {
    --page: #ffffff;
    --card-dark: #15191e;
    --card-mid: #2a323c;
    --card-sheen: #3d4855;
    --name-gold: #f4c21a;
    --line-gold: #e7b94a;
    --swoosh-gold: #f6c200;
    --text-light: #f2f2f2;
    --rose: #f1d3dc;
    --icon-rose: #d9a9b8;
    --photo-a: #7c6f68;
    --photo-b: #2d2a2c;
    --photo-c: #2c8fd0;
  }
  * { margin: 0; padding: 0; box-sizing: border-box; }
  html, body { width: 1200px; height: 900px; overflow: hidden; background: var(--page); }
  body { position: relative; font-family: "Figtree", Arial, sans-serif; }

  .card {
    position: absolute; width: 461px; height: 263px; overflow: hidden;
    background:
      repeating-linear-gradient(180deg, rgba(255,255,255,0.035) 0 1px, transparent 1px 3px),
      radial-gradient(ellipse 70% 30% at 60% 100%, rgba(120,140,160,0.28), transparent 70%),
      radial-gradient(ellipse 60% 40% at 30% 20%, rgba(90,105,125,0.35), transparent 70%),
      linear-gradient(180deg, var(--card-mid) 0%, var(--card-dark) 55%, var(--card-mid) 100%);
    box-shadow: 10px 12px 16px rgba(0,0,0,0.35);
  }
  .card--back-a { left: 113px; top: 168px; }
  .card--front  { left: 632px; top: 168px; }
  .card--back-b { left: 113px; top: 473px; }
  .card--back-c { left: 632px; top: 473px; }

  .portrait { position: absolute; left: 0; top: 0; width: 461px; height: 263px; }

  .agent-name {
    position: absolute; left: 234px; top: 60px;
    font-size: 20px; font-weight: 400; color: var(--name-gold); white-space: nowrap;
  }
  .agent-title, .agent-license {
    position: absolute; font-size: 13px; color: var(--text-light); white-space: nowrap;
  }
  .agent-title { left: 240px; top: 79px; }
  .agent-license { left: 242px; top: 91px; }

  .contact { position: absolute; display: flex; align-items: center; gap: 6px;
    color: var(--text-light); white-space: nowrap; font-size: 13px; }
  .contact svg { width: 9px; height: 9px; flex: none; }
  .contact--cell  { left: 247px; top: 118px; }
  .contact--fax   { left: 245px; top: 138px; }
  .contact--email { left: 238px; top: 158px; font-size: 11.5px; }
  .contact--web   { left: 225px; top: 177px; }

  .address { position: absolute; left: 198px; top: 203px; display: flex; gap: 7px;
    color: var(--text-light); font-size: 11px; line-height: 13px; }
  .address svg { width: 10px; height: 11px; margin-top: 1px; }

  .brand { position: absolute; left: 0; width: 461px; text-align: center; }
  .brand__name { top: 98px; font-size: 27px; font-weight: 400; letter-spacing: 1px; color: var(--rose); }
  .brand__rule { position: absolute; left: 118px; top: 165px; width: 224px; height: 2px; background: var(--line-gold); }
  .brand__agent { top: 177px; font-size: 18.5px; font-weight: 300; color: var(--rose); }
</style>
</head>
<body>

<svg width="0" height="0" style="position:absolute">
  <defs>
    <linearGradient id="photo-tone" x1="0" y1="0" x2="0" y2="1">
      <stop offset="0" stop-color="var(--photo-a)"/>
      <stop offset="0.55" stop-color="var(--photo-b)"/>
      <stop offset="1" stop-color="var(--photo-c)"/>
    </linearGradient>
    <symbol id="icon-phone" viewBox="0 0 10 10"><rect x="2.5" y="0.5" width="5" height="9" rx="1" fill="none" stroke="var(--icon-rose)"/></symbol>
    <symbol id="icon-fax" viewBox="0 0 10 10"><rect x="0.5" y="3" width="9" height="6" fill="none" stroke="var(--icon-rose)"/><rect x="3" y="0.5" width="4" height="3" fill="none" stroke="var(--icon-rose)"/></symbol>
    <symbol id="icon-mail" viewBox="0 0 10 10"><rect x="0.5" y="2" width="9" height="6.5" fill="none" stroke="var(--icon-rose)"/><path d="M0.5 2 L5 6 L9.5 2" fill="none" stroke="var(--icon-rose)"/></symbol>
    <symbol id="icon-web" viewBox="0 0 10 10"><circle cx="5" cy="5" r="4.5" fill="none" stroke="var(--icon-rose)"/><path d="M0.5 5 H9.5 M5 0.5 V9.5" stroke="var(--icon-rose)"/><ellipse cx="5" cy="5" rx="2" ry="4.5" fill="none" stroke="var(--icon-rose)"/></symbol>
    <symbol id="icon-pin" viewBox="0 0 10 11"><path d="M5 10.5 C2 7 1 5.5 1 4 A4 4 0 0 1 9 4 C9 5.5 8 7 5 10.5 Z" fill="none" stroke="var(--text-light)"/><circle cx="5" cy="4" r="1.4" fill="none" stroke="var(--text-light)"/></symbol>
  </defs>
</svg>

<!-- Back, option A -->
<section class="card card--back-a">
  <svg class="portrait" viewBox="0 0 461 263" role="img" aria-label="Portrait photo of the agent">
    <path d="M11 11 H110 A102 102 0 0 1 110 216 H11 Z" fill="url(#photo-tone)"/>
  </svg>
  <p class="agent-name">Mirela Jostad</p>
  <p class="agent-title">REALTOR</p>
  <p class="agent-license">license 07418923</p>
  <p class="contact contact--cell"><svg><use href="#icon-phone"/></svg>555.218.4790</p>
  <p class="contact contact--fax"><svg><use href="#icon-fax"/></svg>555.634.0182</p>
  <p class="contact contact--email"><svg><use href="#icon-mail"/></svg>mirela.jostad@kelvanehomes.example</p>
  <p class="contact contact--web"><svg><use href="#icon-web"/></svg>kelvanehomes.example</p>
  <div class="address"><svg><use href="#icon-pin"/></svg><p>812 Larkmoor DR.<br>Vista Calif. 92000</p></div>
</section>

<!-- Front -->
<section class="card card--front">
  <p class="brand brand__name">KELVANE HOMES</p>
  <div class="brand__rule"></div>
  <p class="brand brand__agent">Mirela Jostad</p>
</section>

<!-- Back, option B -->
<section class="card card--back-b">
  <svg class="portrait" viewBox="0 0 461 263" role="img" aria-label="Portrait photo of the agent">
    <path d="M11 216 L11 110 Q18 22 100 18 Q165 22 180 110 L196 150 Q150 214 11 216 Z" fill="url(#photo-tone)"/>
    <path d="M11 216 Q150 224 206 150 Q224 105 200 61" fill="none" stroke="var(--swoosh-gold)" stroke-width="5" stroke-linecap="round"/>
  </svg>
  <p class="agent-name">Mirela Jostad</p>
  <p class="agent-title">REALTOR</p>
  <p class="agent-license">license 07418923</p>
  <p class="contact contact--cell"><svg><use href="#icon-phone"/></svg>555.218.4790</p>
  <p class="contact contact--fax"><svg><use href="#icon-fax"/></svg>555.634.0182</p>
  <p class="contact contact--email"><svg><use href="#icon-mail"/></svg>mirela.jostad@kelvanehomes.example</p>
  <p class="contact contact--web"><svg><use href="#icon-web"/></svg>kelvanehomes.example</p>
  <div class="address"><svg><use href="#icon-pin"/></svg><p>812 Larkmoor DR.<br>Vista Calif. 92000</p></div>
</section>

<!-- Back, option C -->
<section class="card card--back-c">
  <svg class="portrait" viewBox="0 0 461 263" role="img" aria-label="Portrait photo of the agent">
    <path d="M11 216 L11 110 Q18 22 100 18 Q165 22 178 115 L192 170 Q130 214 11 216 Z" fill="url(#photo-tone)"/>
  </svg>
  <p class="agent-name">Mirela Jostad</p>
  <p class="agent-title">REALTOR</p>
  <p class="agent-license">license 07418923</p>
  <p class="contact contact--cell"><svg><use href="#icon-phone"/></svg>555.218.4790</p>
  <p class="contact contact--fax"><svg><use href="#icon-fax"/></svg>555.634.0182</p>
  <p class="contact contact--email"><svg><use href="#icon-mail"/></svg>mirela.jostad@kelvanehomes.example</p>
  <p class="contact contact--web"><svg><use href="#icon-web"/></svg>kelvanehomes.example</p>
  <div class="address"><svg><use href="#icon-pin"/></svg><p>812 Larkmoor DR.<br>Vista Calif. 92000</p></div>
</section>

</body>
</html>
```